Threadly and Pixomane advertisment

Create a advertisement for Threadly and Pixomane
Text:
Introducing KELVO
Speeds to 500 Mbps
Packages start at only $89.99 monthly for speeds to 100Mbps
Check out our Brisket for the Holidays Event, FREE Equipment, FREE Installation, FREE wifi6 router and first month of service FREE!

```html
<!DOCTYPE html>
<html lang="en">
<head>
<meta charset="utf-8">
<title>KELVO – Speeds to 500 Mbps</title>
<link rel="stylesheet" href="https://fonts.googleapis.com/css2?family=Barlow:ital,wght@0,500;0,600;0,700;1,500;1,600&family=Barlow+Semi+Condensed:wght@600;700&display=swap">
<style>
  :root {
    --white: #ffffff;
    --ink: #101418;
    --navy: #0a0f1c;
    --band-blue: #1f4fa3;
    --red: #ec1f3a;
    --cyan: #22b6ee;
    --sky-deep: #0b2a45;
    --sky-teal: #1fb6b4;
    --snow: #c9dbe6;
  }
  html, body {
    margin: 0;
    padding: 0;
    width: 1200px;
    height: 1200px;
    overflow: hidden;
    background: var(--navy);
  }
  .ad {
    position: relative;
    width: 1200px;
    height: 1200px;
    overflow: hidden;
    font-family: "Barlow", "Arial", sans-serif;
  }
  .scene-photo {
    position: absolute;
    inset: 0;
    background:
      radial-gradient(ellipse 60% 45% at 18% 12%, rgba(60, 230, 220, 0.9), transparent 70%),
      radial-gradient(ellipse 40% 60% at 55% 30%, rgba(40, 200, 200, 0.55), transparent 70%),
      linear-gradient(180deg, var(--sky-teal) 0%, #146a86 30%, var(--sky-deep) 55%, #3f6c88 70%, var(--snow) 78%, #1d4462 90%);
  }
  .brand-tab {
    position: absolute;
    top: 0;
    right: 0;
    width: 500px;
    height: 160px;
  }
  .brand-name {
    position: absolute;
    top: 70px;
    right: 64px;
    display: flex;
    align-items: center;
    gap: 12px;
    font-weight: 600;
    font-size: 40px;
    color: var(--ink);
    white-space: nowrap;
  }
  .brand-dot {
    width: 14px;
    height: 14px;
    border-radius: 50%;
    background: var(--red);
  }
  .intro {
    position: absolute;
    left: 72px;
    top: 168px;
    margin: 0;
    font-weight: 700;
    font-size: 58px;
    letter-spacing: 6px;
    color: var(--ink);
  }
  .headline {
    position: absolute;
    left: 0;
    top: 0;
    width: 1200px;
    height: 1200px;
  }
  .headline text {
    fill: var(--white);
  }
  .product-name {
    font-family: "Barlow", "Arial", sans-serif;
    font-weight: 600;
    font-size: 390px;
  }
  .speed-line {
    font-family: "Barlow Semi Condensed", "Arial Narrow", sans-serif;
    font-weight: 700;
    font-size: 118px;
  }
  .offer-band {
    position: absolute;
    left: 0;
    top: 0;
    width: 1200px;
    height: 1200px;
  }
  .event-note {
    position: absolute;
    left: 39px;
    top: 966px;
    margin: 0;
    font-style: italic;
    font-weight: 600;
    font-size: 16.5px;
    color: var(--cyan);
    text-transform: uppercase;
    white-space: nowrap;
  }
  .event-note .event-name { color: var(--red); }
  .free-word {
    position: absolute;
    left: 36px;
    top: 986px;
    margin: 0;
    font-family: "Barlow Semi Condensed", "Arial Narrow", sans-serif;
    font-weight: 700;
    font-size: 124px;
    line-height: 1;
    color: var(--white);
  }
  .free-list {
    position: absolute;
    left: 276px;
    top: 1002px;
    margin: 0;
    padding: 0;
    list-style: none;
    font-weight: 500;
    font-size: 30px;
    line-height: 39px;
    color: var(--white);
  }
  .free-list li {
    display: flex;
    align-items: center;
    gap: 12px;
  }
  .free-list li::before {
    content: "";
    width: 9px;
    height: 9px;
    border-radius: 50%;
    background: var(--white);
    box-shadow: 0 0 0 3px var(--red);
  }
  .first-month {
    position: absolute;
    left: 39px;
    top: 1124px;
    margin: 0;
    font-family: "Barlow Semi Condensed", "Arial Narrow", sans-serif;
    font-weight: 700;
    font-size: 27px;
    color: var(--red);
    white-space: nowrap;
  }
  .offer-divider {
    position: absolute;
    left: 511px;
    top: 958px;
    width: 2px;
    height: 222px;
    background: var(--white);
  }
  .price-block {
    position: absolute;
    left: 545px;
    top: 966px;
    color: var(--white);
  }
  .price-lead {
    margin: 0;
    font-style: italic;
    font-weight: 500;
    font-size: 16.5px;
    white-space: nowrap;
  }
  .price-amount {
    margin: 8px 0 0;
    font-family: "Barlow Semi Condensed", "Arial Narrow", sans-serif;
    font-weight: 700;
    font-size: 68px;
    line-height: 0.9;
    color: var(--red);
  }
  .price-period {
    margin: 0;
    font-family: "Barlow Semi Condensed", "Arial Narrow", sans-serif;
    font-weight: 700;
    font-size: 44px;
    line-height: 1;
    color: var(--cyan);
  }
  .price-speed {
    margin: 4px 0 0;
    font-family: "Barlow Semi Condensed", "Arial Narrow", sans-serif;
    font-weight: 600;
    font-size: 36px;
    line-height: 1;
  }
  .speed-badge {
    position: absolute;
    left: 0;
    top: 0;
    width: 1200px;
    height: 1200px;
  }
  .badge-number {
    font-family: "Barlow Semi Condensed", "Arial Narrow", sans-serif;
    font-weight: 700;
    font-size: 146px;
    fill: var(--white);
  }
  .badge-unit {
    font-family: "Barlow Semi Condensed", "Arial Narrow", sans-serif;
    font-weight: 700;
    font-size: 40px;
    fill: var(--red);
  }
</style>
</head>
<body>
<main class="ad">
  <div class="scene-photo" role="img" aria-label="Photo of green northern lights over snowy mountains under a starry night sky"></div>

  <svg class="brand-tab" viewBox="0 0 500 160" aria-hidden="true">
    <path d="M0 0 H500 V160 H120 C80 160 70 140 55 100 C40 50 30 20 0 20 Z" fill="var(--white)"/>
  </svg>
  <div class="brand-name"><span class="brand-dot"></span>Solwave Satellite</div>

  <h2 class="intro">INTRODUCING</h2>

  <svg class="headline" viewBox="0 0 1200 1200">
    <text class="product-name" x="72" y="555" textLength="1046" lengthAdjust="spacingAndGlyphs">KELVO</text>
    <rect x="77" y="638" width="1043" height="5" fill="var(--ink)"/>
    <text class="speed-line" x="74" y="767" textLength="1046" lengthAdjust="spacingAndGlyphs">SPEEDS TO 500 MBPS</text>
  </svg>

  <svg class="offer-band" viewBox="0 0 1200 1200" aria-hidden="true">
    <path d="M0 940 C300 880 700 860 1200 930 V1200 H0 Z" fill="var(--band-blue)"/>
    <path d="M0 952 C300 894 700 876 1200 946 V1200 H0 Z" fill="var(--navy)"/>
  </svg>

  <p class="event-note">Check out our <span class="event-name">Brisket</span> for the Holidays Event</p>
  <p class="free-word">FREE</p>
  <ul class="free-list">
    <li>EQUIPMENT</li>
    <li>INSTALLATION</li>
    <li>WIFI ROUTER</li>
  </ul>
  <p class="first-month">FIRST MONTH OF SERVICE, FREE!</p>

  <div class="offer-divider"></div>

  <div class="price-block">
    <p class="price-lead">PACKAGES START AT ONLY</p>
    <p class="price-amount">$89.99</p>
    <p class="price-period">MONTHLY</p>
    <p class="price-speed">FOR SPEEDS TO</p>
  </div>

  <svg class="speed-badge" viewBox="0 0 1200 1200">
    <circle cx="1082" cy="1088" r="244" fill="var(--red)"/>
    <text class="badge-number" x="898" y="1067" textLength="226" lengthAdjust="spacingAndGlyphs">100</text>
    <g fill="none" stroke="var(--white)" stroke-width="5" opacity="0.45">
      <polyline points="906,1100 922,1119 906,1138"/>
      <polyline points="928,1100 944,1119 928,1138"/>
      <polyline points="950,1100 966,1119 950,1138"/>
    </g>
    <path d="M962 1096 H1124 L1146 1119 L1124 1142 H962 L978 1119 Z" fill="var(--white)"/>
    <text class="badge-unit" x="1016" y="1135">MBPS</text>
  </svg>
</main>
</body>
</html>
```